About the book: It is an A5 size book, small 40 pages miniguide
Book title: The pocket handbook of home lending
Book subtitle: The quiet road to plenty
Author: Ned Pargiter
Back cover content: Please see attached word document "back page"
Colours: Our company logo should go at the back of the book. One colour we can't use is red. As this is a finance book the red colour is seen negatively. may be light green? you are the expert.
I think lots of white space will work well.
NOTE: please read the back cover notes to get an understanding of what the book is about. It educates readers about finance in property investing. It makes sense that image used combines 'property' and 'finance'. please read back page document attached.
NOTE: it is a small A5 , 40 page book . Its a miniguide rather than a book .

Reason: Dear designers, Thank you for submitting your work over the last few days. Unfortunately we haven't been able to get back to you regarding the final selection of design as the Author of the book has been away on leave with his family without reliable internet access. He is now back and will be giving feedback as we go. We apologise for the time extension. Unfortunately the site didn’t allow me to limit the extension for less than 5 days but we may not require that long. Thanks again. Lulu

Reason: We apologies we hadn't finalized a decision on this project due to the person from our end being away. We would like to finalise this design as soon as possible.

Target Market(s)

22 - 45 age group. Most fall between 30-40. Both male and female. couples , individuals etc ...

Industry/Entity Type

Finance

Font styles to use
Other font styles liked:
• sabon/Aeriel. Let me know if any other suggestions.

Requirements
Nice to have
• use green colour if possible but not essential.

```html
<!DOCTYPE html>
<html lang="en">
<head>
<meta charset="utf-8">
<title>The Pocket Handbook of Home Lending — Cover</title>
<link rel="stylesheet" href="https://fonts.googleapis.com/css2?family=Anton&family=Roboto:wght@300;500;900&display=swap">
<style>
  :root {
    --stage: #4a4a4a;
    --paper: #fbfbfb;
    --ink: #111111;
    --accent: #3f9a52;
    --accent-soft: #8cc79a;
    --rule: #3a3a3a;
    --spine: #0d0d0d;
  }
  * { margin: 0; padding: 0; box-sizing: border-box; }
  html, body { width: 1200px; height: 1148px; overflow: hidden; background: var(--stage); }
  .canvas { position: relative; width: 1200px; height: 1148px; }
  .cover {
    position: absolute; left: 240px; top: 64px; width: 720px; height: 1020px;
    background: var(--paper); overflow: hidden;
  }
  .cover__band {
    position: absolute; top: 0; right: 0; width: 42px; height: 100%; background: var(--spine);
  }
  .brand {
    position: absolute; left: 64px; top: 58px; display: flex; align-items: center; gap: 12px;
    font-family: "Roboto", sans-serif; font-weight: 500; font-size: 26px; color: var(--ink);
  }
  .brand__dot { width: 22px; height: 22px; border-radius: 50%; background: var(--accent); }
  .top-rule {
    position: absolute; left: 36px; top: 138px; width: 600px; height: 4px; background: var(--accent);
  }
  .cover-illustration {
    position: absolute; left: 70px; top: 196px; width: 170px; height: 160px;
    background: linear-gradient(160deg, var(--accent-soft), var(--accent));
  }
  .title {
    position: absolute; left: 64px; top: 380px;
    font-family: "Anton", sans-serif; font-weight: 400; text-transform: uppercase;
    font-size: 112px; line-height: 0.98; color: var(--ink); letter-spacing: 1px;
  }
  .title__line { display: block; }
  .title__line--accent { color: var(--accent); }
  .subtitle {
    position: absolute; left: 64px; top: 862px; width: 560px;
    border-top: 2px solid var(--rule); border-bottom: 2px solid var(--rule);
    padding: 10px 0 12px;
    font-family: "Roboto", sans-serif; font-weight: 300; font-size: 44px; color: var(--ink);
  }
  .author {
    position: absolute; left: 64px; top: 950px;
    font-family: "Roboto", sans-serif; font-weight: 900; font-size: 40px;
    text-transform: uppercase; color: var(--accent); letter-spacing: 1px;
  }
</style>
</head>
<body>
<main class="canvas">
  <article class="cover">
    <div class="brand"><span class="brand__dot"></span><span class="brand__name">Harbourline Capital</span></div>
    <div class="top-rule"></div>

    <div class="cover-illustration" role="img" aria-label="Illustration of a house with a dollar sign"></div>

    <h1 class="title">
      <span class="title__line">The Pocket</span>
      <span class="title__line title__line--accent">Handbook</span>
      <span class="title__line">Of Home</span>
      <span class="title__line">Lending</span>
    </h1>

    <p class="subtitle">The Quiet Road To Plenty</p>
    <p class="author">Ned Pargiter</p>

    <div class="cover__band"></div>
  </article>
</main>
</body>
</html>
```